Business Card Design

Just looking for a good designs that looks good with our company logo. I'd like it to be simple and to the point. Just including contact information, our logo, and my name somewhere on the card so future clients know who they're contacting, and a couple services offered. The two images I attached are pictures of our logo. I don't care which color they they are, I just attached both images to give a reference of logo colors depending on the color of the card.
Names: Calvin Prewitt
Phone: 555-247-9061
Email: tidyturfcrew@mailvista.net
Services offered:
Mowing
Fertilization
Aeration
Bed & tree maintenance
and more.
Industry/Entity Type
Business
Contact Information for Business Card
Names: Calvin Prewitt
Phone: 555-247-9061
Look and feel

```html
<!DOCTYPE html>
<html lang="en">
<head>
<meta charset="utf-8">
<title>Tidy Turf Crew – Business Card</title>
<link href="https://fonts.googleapis.com/css2?family=Roboto+Slab:wght@300;400&display=swap" rel="stylesheet">
<style>
  :root {
    --backdrop: #e6e7ea;
    --card: #f1f1f2;
    --ink: #25272c;
    --charcoal: #32343c;
    --slate: #8a8c92;
    --tomato: #e04a32;
    --paper-white: #ffffff;
  }
  * { box-sizing: border-box; margin: 0; padding: 0; }
  html, body {
    width: 1200px; height: 828px; overflow: hidden;
    background: var(--backdrop);
    font-family: "Roboto Slab", Georgia, serif;
  }
  .canvas {
    width: 1200px; height: 828px;
    display: flex; align-items: center; justify-content: center;
  }
  .business-card {
    position: relative;
    width: 1050px; height: 600px;
    background: var(--card);
    overflow: hidden;
    box-shadow: 0 10px 30px rgba(0,0,0,.12);
  }
  .corner-swoosh { position: absolute; top: 0; right: 0; width: 1050px; height: 240px; }
  .brand {
    position: absolute; left: 70px; top: 235px;
    display: flex; align-items: center; gap: 20px;
  }
  .brand-dot {
    width: 54px; height: 54px; border-radius: 50%;
    background: var(--tomato);
  }
  .brand-name {
    font-size: 46px; font-weight: 400; color: var(--charcoal);
    letter-spacing: 1px;
  }
  .services {
    position: absolute; left: 570px; top: 205px;
    color: var(--ink); font-size: 30px; line-height: 1.32;
  }
  .services-title { font-weight: 400; }
  .services-list { list-style: none; }
  .services-list li { position: relative; padding-left: 30px; }
  .services-list li::before {
    content: ""; position: absolute; left: 4px; top: 17px;
    width: 9px; height: 9px; border-radius: 50%; background: var(--tomato);
  }
  .services-list li.more { padding-left: 30px; }
  .services-list li.more::before { display: none; }
  .holder-name {
    position: absolute; left: 60px; top: 440px;
    font-size: 36px; color: var(--ink);
  }
  .contact-band {
    position: absolute; left: 0; bottom: 0; width: 100%; height: 92px;
    background: var(--charcoal);
    display: flex; align-items: center;
    color: var(--paper-white); font-weight: 300; font-size: 30px;
  }
  .contact-item { display: flex; align-items: center; gap: 22px; }
  .contact-phone { margin-left: 60px; }
  .contact-email { position: absolute; left: 570px; }
  .contact-icon { width: 26px; height: 34px; }
</style>
</head>
<body>
<main class="canvas">
  <section class="business-card">
    <svg class="corner-swoosh" viewBox="0 0 1050 240" aria-hidden="true">
      <path d="M600 0 C 690 140 870 195 1050 175 L1050 200 C 860 222 670 170 585 0 Z" fill="#b9bbc0"/>
      <path d="M620 0 C 705 125 875 175 1050 158 L1050 182 C 865 200 690 150 600 0 Z" fill="var(--charcoal)"/>
      <path d="M638 0 L1050 0 L1050 148 C 880 165 715 118 638 0 Z" fill="var(--tomato)"/>
    </svg>

    <div class="brand">
      <span class="brand-dot"></span>
      <span class="brand-name">Tidy Turf Crew</span>
    </div>

    <div class="services">
      <p class="services-title">Services Offered</p>
      <ul class="services-list">
        <li>Mowing</li>
        <li>Fertilization</li>
        <li>Aeration</li>
        <li>Bed &amp; tree maintenance</li>
        <li class="more">and more.</li>
      </ul>
    </div>

    <p class="holder-name">Calvin Prewitt</p>

    <div class="contact-band">
      <div class="contact-item contact-phone">
        <svg class="contact-icon" viewBox="0 0 26 34" aria-hidden="true">
          <rect x="3" y="1.5" width="20" height="31" rx="3" fill="none" stroke="#fff" stroke-width="2"/>
          <line x1="3" y1="7" x2="23" y2="7" stroke="#fff" stroke-width="1.5"/>
          <line x1="3" y1="26" x2="23" y2="26" stroke="#fff" stroke-width="1.5"/>
          <circle cx="13" cy="29.3" r="1.4" fill="#fff"/>
        </svg>
        <span>555-247-9061</span>
      </div>
      <div class="contact-item contact-email">
        <svg class="contact-icon" viewBox="0 0 26 34" aria-hidden="true">
          <rect x="1" y="9" width="24" height="16" fill="none" stroke="#fff" stroke-width="2"/>
          <polyline points="1,9 13,19 25,9" fill="none" stroke="#fff" stroke-width="2"/>
        </svg>
        <span>tidyturfcrew@mailvista.net</span>
      </div>
    </div>
  </section>
</main>
</body>
</html>
```